Just Sold Postcard

Real Estate/ Thornwick Dale Realty.I'd like a template that I can use to change out the picture of the home, verbiage on the front, and address. I'm including a picture of what I've used in the past. I like designs that use red, with some blue and white. I'd like the ability to change the verbiage on the back as well.

Industry/Entity Type

Real Estate

Font styles to use
Serif
Sans Serif

```html
<!DOCTYPE html>
<html lang="en">
<head>
<meta charset="utf-8">
<title>Just Sold Postcard – Thornwick Dale Realty</title>
<link rel="stylesheet" href="https://fonts.googleapis.com/css2?family=Saira+Condensed:wght@600;700&family=Saira:wght@400;500&display=swap">
<style>
  :root {
    --red: #e8262b;
    --blue: #3b3f9c;
    --navy: #2b2f7e;
    --ink: #3a3a3a;
    --white: #ffffff;
    --panel: #f1f1f1;
    --page: #ecebe8;
    --stamp: #d6d6d6;
  }
  * { margin: 0; padding: 0; box-sizing: border-box; }
  html, body { width: 825px; height: 1200px; overflow: hidden; background: var(--page); }
  body { position: relative; font-family: "Saira", sans-serif; }

  .card { position: absolute; left: 80px; width: 667px; height: 516px; background: var(--white); overflow: hidden; box-shadow: 0 2px 8px rgba(0,0,0,.18); }
  .card--front { top: 64px; }
  .card--back { top: 628px; }
  .card__art { position: absolute; inset: 0; }
  .abs { position: absolute; white-space: nowrap; }

  .heading { font-family: "Saira Condensed", sans-serif; font-weight: 700; text-transform: uppercase; line-height: 1; }

  /* front */
  .agent-panel { left: 32px; top: -4px; width: 288px; height: 425px; background: linear-gradient(#fff 0%, var(--panel) 60%, #e4e4e4 100%); border: 3px solid var(--red); border-top: none; border-radius: 0 0 28px 28px; box-shadow: 0 10px 10px -6px rgba(0,0,0,.35); }
  .brand { left: 47px; top: 24px; width: 257px; height: 97px; background: var(--white); display: flex; align-items: center; justify-content: center; gap: 10px; }
  .brand__mark { width: 14px; height: 14px; background: var(--red); }
  .brand__name { font-family: "Saira", sans-serif; font-weight: 500; font-size: 22px; color: var(--navy); }
  .address { left: 32px; width: 288px; text-align: center; font-size: 46px; }
  .address--line1 { top: 146px; color: var(--red); }
  .address--line2 { top: 194px; color: var(--ink); }
  .ribbon { left: 15px; top: 273px; width: 322px; height: 56px; background: var(--red); color: var(--white); font-size: 40px; display: flex; align-items: center; justify-content: center; box-shadow: 0 3px 4px rgba(0,0,0,.25); }
  .tagline { left: 32px; width: 288px; top: 343px; text-align: center; font-size: 17px; color: var(--ink); }
  .front-phone { left: 32px; width: 288px; top: 370px; text-align: center; font-size: 19px; color: var(--navy); }
  .sold-title { right: 27px; top: 352px; width: 292px; text-align: right; font-size: 30px; font-weight: 600; color: var(--white); }
  .sold-copy { right: 27px; top: 392px; width: 300px; text-align: right; font-size: 14.5px; line-height: 17px; color: var(--white); white-space: normal; }
  .web-bar { left: 0; bottom: 0; width: 667px; height: 52px; background: var(--red); color: var(--white); font-size: 15.5px; font-weight: 500; display: flex; align-items: center; justify-content: center; letter-spacing: .2px; }

  /* back */
  .stamp { left: 571px; top: 26px; width: 68px; height: 68px; background: var(--stamp); }
  .back-name { left: 31px; top: 72px; font-size: 46px; font-weight: 600; color: var(--white); }
  .back-phone { left: 31px; top: 120px; font-size: 23px; color: var(--white); }
  .pitch { left: 33px; top: 210px; font-size: 27px; line-height: 35px; color: var(--white); }
  .pitch__dark { color: #4a2a2a; font-size: 28px; }
  .pitch__small { font-size: 23px; }
  .contact-pill { left: 34px; top: 330px; width: 241px; height: 72px; background: linear-gradient(#fff, #e6e6e6); border-radius: 10px; padding: 10px 0 0 12px; box-shadow: 0 3px 4px rgba(0,0,0,.25); }
  .contact-pill__phone { font-size: 27px; font-weight: 600; color: var(--ink); }
  .contact-pill__email { font-size: 16.5px; color: var(--navy); margin-top: 2px; }
</style>
</head>
<body>

<section class="card card--front">
  <svg class="card__art" width="667" height="516" viewBox="0 0 667 516">
    <defs>
      <linearGradient id="photo-tone" x1="0" y1="0" x2="0" y2="1">
        <stop offset="0" stop-color="#9fc0dd"/>
        <stop offset=".55" stop-color="#b8ad9c"/>
        <stop offset="1" stop-color="#4f8a3a"/>
      </linearGradient>
      <linearGradient id="blue-field" x1="0" y1="0" x2="0" y2="1">
        <stop offset="0" stop-color="#4a4fae"/>
        <stop offset="1" stop-color="#33378f"/>
      </linearGradient>
    </defs>
    <path d="M0 215 Q200 292 330 300 Q530 302 667 232 L667 458 L0 458 Z" fill="url(#blue-field)"/>
    <path role="img" aria-label="Photograph of the sold two-storey home with lit windows, stone porch and front lawn" d="M330 0 H667 V226 Q540 292 380 294 L330 294 Z" fill="url(#photo-tone)"/>
    <path d="M350 302 Q540 298 667 238" fill="none" stroke="#ffffff" stroke-width="10"/>
    <path d="M350 296 Q540 292 667 230" fill="none" stroke="var(--red)" stroke-width="6"/>
    <rect x="0" y="458" width="667" height="6" fill="#ffffff"/>
  </svg>

  <div class="abs agent-panel"></div>
  <div class="abs brand"><span class="brand__mark"></span><span class="brand__name">Thornwick Dale Realty</span></div>
  <div class="abs heading address address--line1">6157 Larkin</div>
  <div class="abs heading address address--line2">Creek Drive</div>
  <div class="abs heading ribbon">Dana Whitfield</div>
  <div class="abs tagline">Your Neighbourhood Expert</div>
  <div class="abs front-phone">Call – 555.014.2290</div>

  <div class="abs heading sold-title">Just Sold Brought Buyer</div>
  <p class="abs sold-copy">Fabulous end unit with granite countertops<br>and hardwood floors, private lot</p>

  <div class="abs web-bar">Please visit our website to know more about us at: www.thornwickdalerealty.com</div>
</section>

<section class="card card--back">
  <svg class="card__art" width="667" height="516" viewBox="0 0 667 516">
    <path d="M0 0 H292 Q322 80 318 184 H0 Z" fill="var(--blue)"/>
    <path d="M300 0 Q334 90 326 186" fill="none" stroke="var(--red)" stroke-width="6"/>
    <path d="M0 189 H324 Q318 330 286 424 H0 Z" fill="var(--red)"/>
    <rect x="0" y="424" width="85" height="92" fill="var(--blue)"/>
  </svg>

  <div class="abs stamp"></div>
  <div class="abs heading back-name">Dana Whitfield</div>
  <div class="abs back-phone">Call – 555.014.2290</div>

  <p class="abs pitch">Contact me today!<br><span class="pitch__dark">For a free market</span><br><span class="pitch__small">Analysis of your home</span></p>

  <div class="abs contact-pill">
    <div class="heading contact-pill__phone">Call - 555.014.2290</div>
    <div class="contact-pill__email">whitfield.dana@mailbox.com</div>
  </div>
</section>

</body>
</html>
```